Criação de Kit com 6 Layouts de Post para Redes Sociais (Facebook, Instagram e etc) para Saúde & Nutrição
" Consultório oftalmológico com ênfase em consultas oftalmológicas, exames complementares e cirurgias oculares "

```html
<!DOCTYPE html>
<html lang="pt-BR">
<head>
<meta charset="UTF-8">
<title>Olhos secos – post</title>
<link href="https://fonts.googleapis.com/css2?family=Montserrat:wght@400;500;600;700;800&display=swap" rel="stylesheet">
<style>
  :root {
    --navy: #1f3569;
    --navy-dark: #17295a;
    --gold: #c9a861;
    --gold-soft: #e3c98e;
    --cream: #f7f1e4;
    --white: #ffffff;
    --text: #2b3a63;
  }
  * { margin: 0; padding: 0; box-sizing: border-box; }
  html, body { width: 1200px; height: 1200px; overflow: hidden; }
  body { font-family: "Montserrat", sans-serif; background: var(--cream); }

  .post {
    position: relative;
    width: 1200px;
    height: 1200px;
    overflow: hidden;
    background: linear-gradient(100deg, #fbf8f1 0%, #f5ecd8 45%, #ead39f 100%);
  }

  .equipment-photo {
    position: absolute;
    left: 0; top: 0;
    width: 760px; height: 420px;
    background: radial-gradient(ellipse at 45% 30%, rgba(190,170,135,.35), rgba(245,237,220,0) 70%);
  }

  .backdrop-word {
    position: absolute;
    left: 1225px; top: -10px;
    font-weight: 800;
    font-size: 220px;
    line-height: 1;
    color: var(--gold-soft);
    opacity: .6;
    transform: rotate(90deg);
    transform-origin: left top;
    white-space: nowrap;
    letter-spacing: -4px;
  }

  .portrait-photo {
    position: absolute;
    left: 540px; top: 40px;
    width: 540px; height: 1160px;
    border-radius: 270px 270px 0 0;
    background: linear-gradient(180deg, #2e2522 0%, #3a2e29 18%, #d9b79b 30%, #e8cdb5 42%, #f1efec 55%, #f5f4f2 100%);
  }

  .headline-tag {
    position: absolute;
    left: 187px; top: 281px;
    background: var(--navy);
    color: var(--white);
    font-weight: 500;
    font-size: 27px;
    line-height: 38px;
    padding: 0 18px;
    letter-spacing: .5px;
  }
  .headline {
    position: absolute;
    left: 185px; top: 322px;
    color: var(--navy);
    font-weight: 700;
    font-size: 88px;
    line-height: 1.1;
    letter-spacing: -1px;
  }
  .intro {
    position: absolute;
    left: 190px; top: 456px;
    width: 420px;
    font-size: 21px;
    line-height: 29px;
    color: var(--text);
  }
  .intro strong { font-weight: 700; color: var(--navy); }

  .info-card {
    position: absolute;
    left: 340px; top: 482px;
    width: 524px; height: 286px;
    background: var(--white);
    border-radius: 26px;
    box-shadow: 0 12px 40px rgba(31,53,105,.12);
    text-align: center;
    padding-top: 20px;
  }
  .info-card h2 {
    color: var(--navy);
    font-weight: 700;
    font-size: 44px;
    line-height: 1.1;
    letter-spacing: -.5px;
  }
  .info-card ul { list-style: none; margin-top: 16px; }
  .info-card li {
    font-size: 19px;
    color: var(--text);
    line-height: 52px;
  }

  .cta {
    position: absolute;
    left: 50%; top: 305px;
    transform: translateX(-50%);
    display: flex; align-items: center; gap: 10px;
    background: var(--navy);
    color: var(--white);
    font-size: 19px;
    font-weight: 500;
    padding: 10px 26px 10px 14px;
    border-radius: 24px;
    white-space: nowrap;
  }

  .brand {
    position: absolute;
    left: 468px; top: 1003px;
    width: 276px; height: 132px;
    background: var(--navy-dark);
    display: flex; align-items: center; justify-content: center; gap: 10px;
  }
  .brand-dot { width: 10px; height: 10px; border-radius: 50%; background: var(--gold); }
  .brand-name {
    color: var(--gold);
    font-weight: 600;
    font-size: 19px;
    letter-spacing: .5px;
    text-transform: uppercase;
    white-space: nowrap;
  }
</style>
</head>
<body>
  <main class="post">
    <div class="equipment-photo" role="img" aria-label="Equipamento oftalmológico desfocado ao fundo"></div>
    <div class="backdrop-word" aria-hidden="true">glaucoma</div>
    <div class="portrait-photo" role="img" aria-label="Mulher de óculos e blusa branca sorrindo com a mão no queixo"></div>

    <p class="headline-tag">COMO PREVENIR O</p>
    <h1 class="headline">glaucoma?</h1>
    <p class="intro"><strong>Consultas oftalmológicas regulares são essenciais,</strong> mesmo na ausência de sintomas, para o diagnóstico precoce da doença.</p>

    <section class="info-card">
      <h2>Olhos secos,<br>o que significam?</h2>
      <ul>
        <li>Deficiência aquosa no filme lacrimal</li>
        <li>Evaporação excessiva do filme lacrimal</li>
        <li>Disfunção das glândulas de Meibomius</li>
      </ul>
      <div class="cta">
        <svg width="26" height="26" viewBox="0 0 26 26" aria-hidden="true">
          <circle cx="13" cy="13" r="12" fill="#ffffff"/>
          <path d="M11 8 l5 5 l-5 5" fill="none" stroke="#1f3569" stroke-width="2.6" stroke-linecap="round" stroke-linejoin="round"/>
        </svg>
        Fale conosco
      </div>
    </section>

    <div class="brand">
      <span class="brand-dot"></span>
      <span class="brand-name">Dra. Helena Marques</span>
    </div>
  </main>
</body>
</html>
```